Brivora Collective Business Card Design

We need a business card design for Brivora Collective. We are a healthcare recruiting, wellness and education company. We partner with medical facilities to find quality candidates. We also offer free wellness courses.
The final design should communicate an emphasis on recruiting and wellness
The main purpose of the business card is to utilized it for networking events, give to hospitals, executives, VCs surgery centers and clinics. I want it to be sleek, clean, use of our brand colors and professional.

```html
<!DOCTYPE html>
<html lang="en">
<head>
<meta charset="utf-8">
<title>Brivora Collective – Business Card</title>
<link rel="stylesheet" href="https://fonts.googleapis.com/css2?family=Questrial&display=swap">
<style>
  :root {
    --brand-green: #02604f;
    --paper: #ffffff;
    --canvas: #eeefef;
    --photo-light: #f6f7f7;
    --photo-mid: #e6eae9;
    --ink-white: #ffffff;
  }
  * { margin: 0; padding: 0; box-sizing: border-box; }
  html, body {
    width: 1200px; height: 1200px; overflow: hidden;
    background: var(--canvas);
    font-family: "Questrial", "Century Gothic", sans-serif;
  }
  .sheet {
    width: 1200px; height: 1200px;
    display: flex; flex-direction: column;
    align-items: center; justify-content: center; gap: 60px;
  }
  .card {
    position: relative;
    width: 900px; height: 514px;
    overflow: hidden;
    box-shadow: 0 6px 18px rgba(0,0,0,0.12);
  }

  /* Front */
  .card--front { background: var(--paper); }
  .front__photo {
    position: absolute; inset: 0;
    background: linear-gradient(115deg, var(--photo-light) 0%, var(--photo-mid) 55%, var(--photo-light) 100%);
    opacity: 0.9;
  }
  .front__brand {
    position: absolute; left: 90px; top: 120px;
    display: flex; align-items: center; gap: 34px;
    color: var(--brand-green);
  }
  .brand-square {
    width: 118px; height: 118px; border-radius: 14px;
    background: var(--brand-green);
  }
  .brand-name {
    font-size: 72px; line-height: 1; letter-spacing: -1px;
  }
  .front__web {
    position: absolute; left: 90px; top: 318px;
    font-size: 28px; letter-spacing: 1px;
    color: var(--brand-green);
  }
  .front__band {
    position: absolute; left: 0; right: 0; bottom: 52px; height: 64px;
    background: var(--brand-green);
  }

  /* Back */
  .card--back { background: var(--brand-green); color: var(--ink-white); }
  .back__details { position: absolute; left: 70px; top: 70px; }
  .back__name { font-size: 50px; line-height: 1.1; }
  .back__rule { width: 420px; height: 2px; background: var(--ink-white); margin: 10px 0 10px; }
  .back__position { font-size: 24px; margin-bottom: 22px; }
  .contact-list { list-style: none; }
  .contact-list li {
    display: flex; align-items: center; gap: 14px;
    font-size: 24px; line-height: 1.6; letter-spacing: 0.5px;
  }
  .contact-icon { width: 18px; height: 18px; flex: none; }
  .back__brand {
    position: absolute; right: 60px; bottom: 56px;
    display: flex; align-items: center; gap: 16px;
    font-size: 30px;
  }
  .back__brand .brand-square { width: 56px; height: 56px; border-radius: 8px; background: var(--ink-white); }
</style>
</head>
<body>
<main class="sheet">
  <section class="card card--front" aria-label="Business card front">
    <div class="front__photo" role="img" aria-label="Faded photograph of healthcare professionals at work"></div>
    <div class="front__brand">
      <span class="brand-square" aria-hidden="true"></span>
      <span class="brand-name">Brivora Collective</span>
    </div>
    <p class="front__web">www.brivoracollective.com</p>
    <div class="front__band"></div>
  </section>

  <section class="card card--back" aria-label="Business card back">
    <div class="back__details">
      <h1 class="back__name">Name Surname</h1>
      <div class="back__rule"></div>
      <p class="back__position">Position</p>
      <ul class="contact-list">
        <li>
          <svg class="contact-icon" viewBox="0 0 24 24" aria-hidden="true"><path fill="#fff" d="M6.6 2.5l3 3.4-1.9 2.4c1.3 2.9 3.6 5.2 6.5 6.6l2.4-1.9 3.4 3-1.6 3.6C10.5 19.2 4.8 13.5 3 5.6z"/></svg>
          <span>123 456 7890</span>
        </li>
        <li>
          <svg class="contact-icon" viewBox="0 0 24 24" aria-hidden="true"><rect x="2" y="5" width="20" height="14" fill="#fff"/><path d="M2 5l10 8 10-8M2 19l8-7M22 19l-8-7" stroke="#02604f" stroke-width="1.6" fill="none"/></svg>
          <span>name@brivoracollective.com</span>
        </li>
        <li>
          <svg class="contact-icon" viewBox="0 0 24 24" aria-hidden="true"><path fill="#fff" d="M12 3l8 16-8-4-8 4z"/></svg>
          <span>www.brivoracollective.com</span>
        </li>
      </ul>
    </div>
    <div class="back__brand">
      <span class="brand-square" aria-hidden="true"></span>
      <span>Brivora Collective</span>
    </div>
  </section>
</main>
</body>
</html>
```